May the Best Business Card Win

I want a business card that goes with the logo. We are an Energy Efficient Home Improvement Company. We want something modern but at the same time professional. This is going on a Black Matte Card so we want to impress everyone.

Front Side:

(Logo)
Lic:472159

Tomas J. Whitley
Founder & Energy Consultant
Tel: (818)555-0134
SolvaHomesCo@[login to view URL]
Larkfield CA 90577

Back Side:
Facebook Logo: SolvaHomesCo
Instagram Logo: SolvaHomesCo
Website Logo: [login to view URL]

Front Side:

(Logo)
Lic:472159

Helena Brochu
Lead Energy Consultant
Tel: (818)555-0192 Office: 818-555-0134
Email: Helenabrochu@[login to view URL]
Address: Larkfield CA 90577

Back Side:

```html
<!DOCTYPE html>
<html lang="en">
<head>
<meta charset="utf-8">
<title>Solva Homes – Business Card</title>
<link rel="stylesheet" href="https://fonts.googleapis.com/css2?family=Montserrat:wght@600;700&family=Lato:wght@400;700&display=swap">
<style>
  :root {
    --page: #ebe8e3;
    --card-black: #000000;
    --lime: #a4c74c;
    --grey: #a6a6a6;
    --ink: #1e1e1e;
    --white: #ffffff;
    --shadow: 0 14px 22px rgba(0,0,0,0.28);
  }
  * { margin: 0; padding: 0; box-sizing: border-box; }
  html, body { width: 1200px; height: 1200px; overflow: hidden; }
  body { background: var(--page); position: relative; font-family: "Lato", sans-serif; }

  .card { position: absolute; left: 223px; width: 754px; height: 427px; background: var(--card-black); box-shadow: var(--shadow); overflow: hidden; }
  .card--front { top: 147px; }
  .card--back { top: 640px; }

  /* front */
  .front__band { position: absolute; left: 0; right: 0; top: 326px; bottom: 0; background: var(--lime); }
  .front__rail { position: absolute; left: 54px; width: 43px; top: 0; bottom: 0; background: var(--grey); }
  .front__rail-accent { position: absolute; left: 54px; width: 43px; top: 140px; height: 186px; background: var(--lime); }
  .icon { position: absolute; left: 65px; width: 21px; height: 21px; fill: var(--ink); }
  .icon--person { top: 69px; }
  .icon--phone { top: 163px; }
  .icon--web { top: 200px; }
  .icon--mail { top: 238px; }

  .person__name { position: absolute; left: 108px; top: 46px; font-family: "Montserrat", sans-serif; font-weight: 700; font-size: 30px; color: var(--white); letter-spacing: 0.2px; white-space: nowrap; }
  .person__title { position: absolute; left: 108px; top: 89px; font-size: 17px; color: var(--white); white-space: nowrap; }
  .rule { position: absolute; left: 102px; width: 238px; height: 2px; background: var(--lime); }
  .rule--top { top: 124px; }
  .rule--bottom { top: 276px; }
  .contact { position: absolute; left: 108px; font-size: 17px; color: var(--white); white-space: nowrap; }
  .contact--phone { top: 162px; }
  .contact--web { top: 199px; }
  .contact--mail { top: 237px; }

  .front__meta { position: absolute; left: 120px; top: 353px; font-size: 17px; color: var(--ink); line-height: 24px; white-space: nowrap; }
  .front__meta strong { font-weight: 700; }

  .brand { position: absolute; display: flex; align-items: center; gap: 10px; }
  .brand__dot { width: 14px; height: 14px; border-radius: 50%; background: var(--lime); }
  .brand__name { font-family: "Montserrat", sans-serif; font-weight: 700; font-size: 28px; color: var(--lime); letter-spacing: 1px; white-space: nowrap; }
  .brand--front { left: 460px; top: 244px; }
  .brand--back { left: 50%; transform: translateX(-50%); top: 214px; }

  /* back */
  .back__band { position: absolute; left: 0; right: 0; top: 351px; bottom: 0; background: var(--lime); }
  .social { position: absolute; left: 35px; display: flex; align-items: center; gap: 9px; font-size: 15px; color: var(--white); }
  .social__mark { width: 22px; height: 22px; border-radius: 50%; background: var(--grey); }
  .social--first { top: 37px; }
  .social--second { top: 69px; }
  .back__site { position: absolute; left: 0; right: 0; top: 368px; text-align: center; font-size: 26px; color: var(--ink); }
</style>
</head>
<body>
  <section class="card card--front">
    <div class="front__band"></div>
    <div class="front__rail"></div>
    <div class="front__rail-accent"></div>

    <svg class="icon icon--person" viewBox="0 0 24 24" aria-hidden="true"><circle cx="12" cy="7" r="5"/><path d="M2 23c0-6 4.5-9 10-9s10 3 10 9z"/></svg>
    <svg class="icon icon--phone" viewBox="0 0 24 24" aria-hidden="true"><path d="M6.6 10.8a15 15 0 0 0 6.6 6.6l2.2-2.2a1 1 0 0 1 1-.25 11.4 11.4 0 0 0 3.6.57 1 1 0 0 1 1 1V20a1 1 0 0 1-1 1A17 17 0 0 1 3 4a1 1 0 0 1 1-1h3.5a1 1 0 0 1 1 1c0 1.25.2 2.450.57 3.57a1 1 0 0 1-.25 1z"/></svg>
    <svg class="icon icon--web" viewBox="0 0 24 24" aria-hidden="true"><path d="M12 2a10 10 0 1 0 0 20 10 10 0 0 0 0-20zm6.9 6h-2.9a15.6 15.6 0 0 0-1.4-3.6A8 8 0 0 1 18.9 8zM12 4c.8 1.2 1.5 2.5 1.9 4h-3.8c.4-1.5 1.1-2.8 1.9-4zM4.3 14a8 8 0 0 1 0-4h3.4a16 16 0 0 0 0 4zm.8 2h2.9c.3 1.3.8 2.5 1.4 3.6A8 8 0 0 1 5.1 16zM8 8H5.1a8 8 0 0 1 4.3-3.6C8.8 5.5 8.3 6.7 8 8zm4 12c-.8-1.2-1.5-2.5-1.9-4h3.8c-.4 1.5-1.1 2.8-1.9 4zm2.3-6H9.7a14 14 0 0 1 0-4h4.6a14 14 0 0 1 0 4zm.3 5.6c.6-1.1 1.1-2.3 1.4-3.6h2.9a8 8 0 0 1-4.3 3.6zm1.7-5.6a16 16 0 0 0 0-4h3.4a8 8 0 0 1 0 4z"/></svg>
    <svg class="icon icon--mail" viewBox="0 0 24 24" aria-hidden="true"><path d="M2 5h20v14H2zm2 2v.5l8 5 8-5V7zm0 2.8V17h16V9.8l-8 5z"/></svg>

    <h1 class="person__name">Tomas J. Whitley</h1>
    <p class="person__title">Founder &amp; Energy Consultant</p>
    <div class="rule rule--top"></div>
    <p class="contact contact--phone">(818)555-0134</p>
    <p class="contact contact--web">www.SolvaHomesCo.com</p>
    <p class="contact contact--mail">SolvaHomesCo@mailhub.com</p>
    <div class="rule rule--bottom"></div>

    <p class="front__meta"><strong>Lic:</strong>472159<br>Larkfield CA 90577</p>

    <div class="brand brand--front"><span class="brand__dot"></span><span class="brand__name">SOLVA HOMES</span></div>
  </section>

  <section class="card card--back">
    <p class="social social--first"><span class="social__mark"></span>SolvaHomesCo</p>
    <p class="social social--second"><span class="social__mark"></span>SolvaHomesCo</p>

    <div class="brand brand--back"><span class="brand__dot"></span><span class="brand__name">SOLVA HOMES</span></div>

    <div class="back__band"></div>
    <p class="back__site">www.SolvaHomesCo.com</p>
  </section>
</body>
</html>
```